依頼詳細
リサイタル、コンサートでの配布を致します。
記載項目
記載内容は、①画像は添付画像を使用、②内容は、添付アンケートの ファンクラブへのご参加について、③最後の事務局表記、をお願いいたします。追加事項がありましたら、個別に修正をお願いいたしますので、よろしくお願い申し上げます。
サイズ
A4
ページ数
片面
希望イメージ
シンプル 複雑
単色 カラフル
暗い 明るい
日常 高級
遊び心 厳粛
未来的 伝統的
女性的 男性的
希望する色
クラッシックなので、エレガントな仕上がりを希望します。
納品ファイル
• 高解像度JPG (.jpg)
• イラストレーター形式 (.ai)
補足説明
デザイン後、そのまま、印刷に出す予定です。イラストレーターと、jpgで頂けると助かります。
クラシック若手ピアニストの藤田沙也さんのファンクラブ Circle.SAYAの入会に関するパンフレットのデザイン依頼です。必要なデータは、添付ファイルにてアップしてあります。不明点がありましたら、ご質問下さい。内容的に、難しいものではございません。よろしくお願いします。

全体のバランス。優雅さ。

沢山の皆さんにご提案いただき嬉しく思います。ありがとうございます!

```html
<!DOCTYPE html>
<html lang="ja">
<head>
<meta charset="UTF-8">
<title>Circle.SAYA ファンクラブ</title>
<link href="https://fonts.googleapis.com/css2?family=Cormorant+Garamond:wght@400;500&family=Noto+Serif+JP:wght@400;500;700&display=swap" rel="stylesheet">
<style>
:root{
  --ink:#0b0a09;
  --paper:#ffffff;
  --muted:#d9d6d0;
  --key:#5a5753;
  --photo-dark:#1a1410;
  --photo-mid:#6b5a4a;
  --photo-light:#c9c1b6;
}
*{margin:0;padding:0;box-sizing:border-box}
html,body{width:846px;height:1200px;overflow:hidden;background:var(--ink)}
body{font-family:"Noto Serif JP",serif;color:var(--paper)}
.poster{position:relative;width:846px;height:1200px;background:var(--ink);overflow:hidden}
.key-strip{position:absolute;top:0;bottom:0;width:30px;background:linear-gradient(90deg,var(--key),#8a8783)}
.key-strip--left{left:0}
.key-strip--right{right:0;background:linear-gradient(90deg,#8a8783,var(--key))}
.hero-photo{position:absolute;left:34px;right:34px;top:0;height:820px;
  background:radial-gradient(ellipse at 62% 40%,var(--photo-light) 0%,var(--photo-mid) 35%,var(--photo-dark) 75%,var(--ink) 100%)}
.launch-badge{position:absolute;left:58px;top:28px;width:118px;height:96px;background:var(--paper);color:var(--ink);
  border-radius:6px;display:flex;flex-direction:column;align-items:center;justify-content:center;text-align:center;
  font-family:"Cormorant Garamond",serif;font-size:19px;line-height:1.1}
.launch-badge strong{font-family:"Noto Serif JP",serif;font-size:24px;font-weight:700;margin-top:4px}
.eyebrow{position:absolute;left:0;right:0;top:826px;text-align:center;font-size:17px;letter-spacing:.12em}
.eyebrow span{font-family:"Cormorant Garamond",serif;margin-right:10px;letter-spacing:.2em}
.title{position:absolute;left:0;right:0;top:846px;text-align:center;font-family:"Cormorant Garamond",serif;
  font-weight:400;font-size:96px;line-height:1;letter-spacing:.04em}
.title small{font-size:72px}
.intro{position:absolute;left:90px;right:90px;top:962px;text-align:center;font-size:14px;line-height:1.7;color:var(--muted)}
.benefits{position:absolute;left:60px;right:60px;top:1028px;display:grid;grid-template-columns:1fr 1fr;row-gap:14px;column-gap:30px}
.benefit-row{display:flex;align-items:center;gap:12px;border-top:1px solid #444;padding-top:8px}
.tag{flex:none;border:1px solid var(--paper);font-size:12px;padding:3px 8px;font-weight:500}
.perk-list{list-style:none;font-size:11px;line-height:1.6;color:var(--muted)}
.fee{font-size:24px;font-weight:500;letter-spacing:.04em}
.footer{position:absolute;left:34px;right:34px;bottom:16px;height:34px;border-top:1px solid #777;border-bottom:1px solid #777;
  display:flex;align-items:center;justify-content:center;font-size:11px;color:var(--muted);letter-spacing:.03em}
</style>
</head>
<body>
<main class="poster">
  <div class="key-strip key-strip--left" role="img" aria-label="Piano keys decoration"></div>
  <div class="key-strip key-strip--right" role="img" aria-label="Piano keys decoration"></div>
  <div class="hero-photo" role="img" aria-label="Photo of the pianist seated at a grand piano in a dark hall"></div>

  <div class="launch-badge">Circle.SAYA<strong>誕生!</strong></div>

  <p class="eyebrow"><span>PIANIST</span>藤田沙也ファンクラブ</p>
  <h1 class="title">C<small>IRCLE</small>.SAYA</h1>

  <p class="intro">この度、藤田沙也ファンクラブ「Circle.SAYA」が立ち上がりましたので皆さまへご案内いたします。<br>ファンクラブに入会すると、下記の特典が受けられます。</p>

  <section class="benefits">
    <div class="benefit-row">
      <span class="tag">普通会員特典</span>
      <ul class="perk-list">
        <li>1. リサイタル・コンサートのチケット先行予約</li>
        <li>2. 会報「Circle.SAYA通信」の送付(不定期)</li>
        <li>3. イベントのお知らせメールの配信(不定期)</li>
      </ul>
    </div>
    <div class="benefit-row">
      <span class="tag">特別会員特典</span>
      <ul class="perk-list">
        <li>1. 限定イベントへのご招待(1回)</li>
        <li>2. リサイタル・コンサートへのご招待(1回)</li>
        <li>3. サイン入りアルバムのプレゼント(1枚)</li>
      </ul>
    </div>
    <div class="benefit-row">
      <span class="tag">普通会員会費</span>
      <span class="fee">年会費無料</span>
    </div>
    <div class="benefit-row">
      <span class="tag">特別会員会費</span>
      <span class="fee">年会費 3,000円</span>
    </div>
  </section>

  <footer class="footer">お申込み・お問い合わせ先 | Circle.SAYA事務局 circle.saya@harmonia-office.jp (担当:森本) / 株式会社ハルモニア http://www.harmonia-office.jp</footer>
</main>
</body>
</html>
```